Quilled Mark website redesign

We have an existing website www.QuilledMarkSubtitles.com that needs design improvements and modernization. We want to keep the basic idea of the pop art and the dialogue balloons.

Target Market(s)

US and Europe media producers

Industry/Entity Type

Media

Coding

Coded - Design and coding required

Number of Pages Required

5+ page

Font styles to use
Other font styles liked:
• Modern font

Requirements
Must have
• current pop art figures, current logo,
Nice to have
• I like the idea of the current website. It just needs improvments and modernization.
Should not have
• No movement necessary

```html
<!DOCTYPE html>
<html lang="en">
<head>
<meta charset="utf-8">
<title>Quilled Mark — Closed Captioning</title>
<link href="https://fonts.googleapis.com/css2?family=Poppins:wght@300;400;500;600;700&display=swap" rel="stylesheet">
<style>
:root{
  --yellow:#f6c41d;
  --teal:#2b7c7e;
  --teal-dark:#1d4f57;
  --ink:#333;
  --muted:#666;
  --grey:#f2f2f2;
  --white:#fff;
}
*{box-sizing:border-box;margin:0;padding:0}
html,body{width:1200px;height:4286px;overflow:hidden}
body{position:relative;font-family:'Poppins',sans-serif;color:var(--ink);background:var(--white)}
.abs{position:absolute}
.center{text-align:center}
.header{left:0;top:0;width:1200px;height:125px;background:var(--yellow)}
.brand{left:86px;top:38px;display:flex;align-items:center;gap:10px;font-weight:600;font-size:26px;color:var(--teal-dark)}
.brand-dot{width:30px;height:30px;border-radius:50%;background:var(--teal-dark)}
.nav a{position:absolute;top:50px;font-size:15px;color:#333;text-decoration:none}
.nav a.active{color:var(--teal);border-bottom:2px solid var(--teal);padding-bottom:4px}
.btn-teal{background:var(--teal);color:#fff;font-size:15px;display:flex;align-items:center;justify-content:center;text-decoration:none}
.hero{left:0;top:125px;width:1200px;height:591px;background:linear-gradient(120deg,#4a4440,#2f2b29 50%,#3b3a32)}
.hero-title{left:0;top:318px;width:1200px;font-size:54px;font-weight:600;color:var(--yellow)}
.hero-sub{left:220px;top:394px;width:760px;font-size:15px;color:#fff;line-height:22px}
.btn-outline{border:1.5px solid #ddd;color:#fff;font-size:18px;display:flex;align-items:center;justify-content:center;text-decoration:none}
.h2{font-size:44px;font-weight:500;color:var(--teal)}
.lead{font-size:15px;color:#555;line-height:23px}
.card{width:338px;height:414px;top:927px;background:#fff;box-shadow:0 3px 10px rgba(0,0,0,.12)}
.card-img{position:absolute;left:7px;top:7px;width:324px;height:170px}
.card h3{position:absolute;left:54px;top:214px;font-size:16px;font-weight:500;color:var(--teal)}
.card ul{position:absolute;left:54px;top:256px;list-style:none}
.card li{display:flex;align-items:center;gap:10px;height:33px;font-size:13px;color:#444}
.tick{width:22px;height:22px}
.about{left:0;top:1440px;width:1200px;height:554px;background:var(--grey)}
.about-text{font-size:15px;line-height:24px;color:#555}
.ready{left:0;top:1994px;width:1200px;height:322px;background:var(--teal-dark)}
.ready-code{left:850px;top:1994px;width:350px;height:322px;background:linear-gradient(90deg,rgba(29,79,87,0),#24606a 40%,#2b6b74)}
.service-icon{width:100px;height:100px}
.service h3{font-size:17px;font-weight:500;color:var(--teal);white-space:nowrap}
.service p{font-size:12.5px;color:#666;line-height:22px}
.partners{left:0;top:2824px;width:1200px;height:160px;background:var(--grey)}
.partner{top:2892px;font-size:20px;font-weight:500;color:#1c5fa8;white-space:nowrap}
.arrow-btn{width:48px;height:48px}
.news{left:0;top:2984px;width:1200px;height:752px;background:#f7f7f7}
.news-card{background:#fff}
.date{font-size:14px;color:#444}
.news-title{font-size:19px;color:var(--teal);line-height:27px}
.news-text{font-size:15px;color:#444;line-height:22px}
.footer{left:0;top:3736px;width:1200px;height:437px;background:var(--teal)}
.footer h4{position:absolute;font-size:20px;font-weight:600;color:#fff}
.footer h4 span{font-weight:400}
.rule{width:40px;height:2px;background:#fff}
.flink{font-size:15px;color:#fff;display:flex;align-items:center;gap:12px}
.contact-row{display:flex;gap:18px;color:#fff;font-size:14.5px;line-height:18px}
.contact-icon{width:34px;height:34px;flex:none}
.bottom{left:0;top:4173px;width:1200px;height:113px;background:var(--yellow)}
.social{width:42px;height:42px}
</style>
</head>
<body>

<header class="abs header">
  <div class="abs brand"><span class="brand-dot"></span>Quilled Mark</div>
  <nav class="nav">
    <a href="#" class="active" style="left:431px">Home</a>
    <a href="#" style="left:516px">About Us</a>
    <a href="#" style="left:621px">Samples &amp; Prices</a>
    <a href="#" style="left:790px">Blogs</a>
    <a href="#" style="left:869px">Talk to Us</a>
  </nav>
  <a class="abs btn-teal" style="left:995px;top:45px;width:120px;height:35px">Contact Us</a>
</header>

<section>
  <div class="abs hero" role="img" aria-label="Photo of a couple working on a laptop on a sofa, dimmed"></div>
  <h1 class="abs hero-title center">We create Broadcast Quality</h1>
  <p class="abs hero-sub center">We strive to deliver the highest levels of service to help you reach your goals. We thank you for to closing, our team is with you every step of the way!</p>
  <a class="abs btn-outline" style="left:486px;top:463px;width:226px;height:51px">Purchase Now</a>
</section>

<section>
  <h2 class="abs h2 center" style="left:0;top:790px;width:1200px">Closed Captioning since 2003</h2>
  <p class="abs lead center" style="left:200px;top:851px;width:800px">Why it makes better sense to do Closed Captioning and CCSL together. Since 2003, Quilled Mark has been providing broadcast quality .</p>

  <div class="abs card" style="left:78px">
    <div class="card-img" role="img" aria-label="Photo of hands arranging script notes on a corkboard" style="background:linear-gradient(135deg,#a67a52,#d9c3a5)"></div>
    <h3>POST PRODUCTION SCRIPT</h3>
    <ul>
      <li><svg class="tick" viewBox="0 0 22 22"><circle cx="11" cy="11" r="11" fill="#f6c41d"/><path d="M6 11.5l3.5 3.5L16 8" stroke="#fff" stroke-width="2.5" fill="none"/></svg>CCSL</li>
      <li><svg class="tick" viewBox="0 0 22 22"><circle cx="11" cy="11" r="11" fill="#f6c41d"/><path d="M6 11.5l3.5 3.5L16 8" stroke="#fff" stroke-width="2.5" fill="none"/></svg>Dialogue List</li>
      <li><svg class="tick" viewBox="0 0 22 22"><circle cx="11" cy="11" r="11" fill="#f6c41d"/><path d="M6 11.5l3.5 3.5L16 8" stroke="#fff" stroke-width="2.5" fill="none"/></svg>As Broadcast Script</li>
    </ul>
  </div>
  <div class="abs card" style="left:429px">
    <div class="card-img" role="img" aria-label="Photo of an editing workstation with glowing monitors" style="background:linear-gradient(135deg,#0d1a3a,#3a2a7a 50%,#8a1a3a)"></div>
    <h3>CLOSED CAPTIONING</h3>
    <ul>
      <li><svg class="tick" viewBox="0 0 22 22"><circle cx="11" cy="11" r="11" fill="#f6c41d"/><path d="M6 11.5l3.5 3.5L16 8" stroke="#fff" stroke-width="2.5" fill="none"/></svg>Broadcast Quality</li>
      <li><svg class="tick" viewBox="0 0 22 22"><circle cx="11" cy="11" r="11" fill="#f6c41d"/><path d="M6 11.5l3.5 3.5L16 8" stroke="#fff" stroke-width="2.5" fill="none"/></svg>Offline Captioning</li>
      <li><svg class="tick" viewBox="0 0 22 22"><circle cx="11" cy="11" r="11" fill="#f6c41d"/><path d="M6 11.5l3.5 3.5L16 8" stroke="#fff" stroke-width="2.5" fill="none"/></svg>Live Captioning</li>
    </ul>
  </div>
  <div class="abs card" style="left:780px">
    <div class="card-img" role="img" aria-label="Photo of a studio microphone" style="background:linear-gradient(135deg,#3a2a20,#7a5a40 60%,#2a2018)"></div>
    <h3>AUDIO DESCRIPTION</h3>
    <ul>
      <li><svg class="tick" viewBox="0 0 22 22"><circle cx="11" cy="11" r="11" fill="#f6c41d"/><path d="M6 11.5l3.5 3.5L16 8" stroke="#fff" stroke-width="2.5" fill="none"/></svg>English</li>
      <li><svg class="tick" viewBox="0 0 22 22"><circle cx="11" cy="11" r="11" fill="#f6c41d"/><path d="M6 11.5l3.5 3.5L16 8" stroke="#fff" stroke-width="2.5" fill="none"/></svg>Spanish</li>
      <li><svg class="tick" viewBox="0 0 22 22"><circle cx="11" cy="11" r="11" fill="#f6c41d"/><path d="M6 11.5l3.5 3.5L16 8" stroke="#fff" stroke-width="2.5" fill="none"/></svg>Audio and Video Files</li>
    </ul>
  </div>
</section>

<section>
  <div class="abs about"></div>
  <div class="abs" role="img" aria-label="Photo of a woman with a mug working at a laptop" style="left:91px;top:1484px;width:440px;height:440px;border-radius:50%;background:linear-gradient(135deg,#e8e4df,#b9b1a8)"></div>
  <div class="abs" role="img" aria-label="Photo of a round badge on a cork board" style="left:378px;top:1792px;width:166px;height:166px;border-radius:50%;border:5px solid #fff;background:radial-gradient(circle,#d9a04a,#2b3a3a 70%)"></div>
  <h2 class="abs h2" style="left:584px;top:1568px">About Us</h2>
  <p class="abs about-text" style="left:582px;top:1640px;width:500px">Since 2003, Quilled Mark has been providing broadcast quality Closed Captioning, Subtitling, Post Production Scripts such as and Television Industry in the US and worldwide.</p>
  <p class="abs about-text" style="left:582px;top:1736px;width:500px">Since 2003, Quilled Mark has been providing broadcast quality Industry in the US and worldwide.</p>
  <a class="abs btn-teal" style="left:589px;top:1807px;width:165px;height:40px">Shop Now</a>
</section>

<section>
  <div class="abs ready"></div>
  <div class="abs ready-code" role="img" aria-label="Photo of CSS code on a screen, tinted teal"></div>
  <h2 class="abs center" style="left:0;top:2064px;width:1200px;font-size:42px;font-weight:500;color:#fff">Ready to Get Started?</h2>
  <p class="abs center" style="left:250px;top:2141px;width:700px;font-size:15px;line-height:23px;color:#fff">Top-notch quality at affordable rates.It doesn't get better than Quilled Mark! redefine the tradition alquality at affordable rates.</p>
  <a class="abs btn-outline" style="left:516px;top:2213px;width:166px;height:42px;font-size:15px">Contact Us</a>
</section>

<section>
  <h2 class="abs h2 center" style="left:0;top:2406px;width:1200px">Our Services</h2>
  <svg class="abs service-icon" style="left:176px;top:2496px" viewBox="0 0 100 100"><circle cx="50" cy="50" r="48" fill="none" stroke="#f6c41d" stroke-dasharray="2 3"/><circle cx="50" cy="50" r="43" fill="#f6c41d"/><path d="M50 30l16 6v12c0 10-7 18-16 22-9-4-16-12-16-22V36z" fill="#fff"/><path d="M50 41l3 6 6 1-4.5 4 1 6-5.5-3-5.5 3 1-6-4.5-4 6-1z" fill="#f6c41d"/></svg>
  <svg class="abs service-icon" style="left:416px;top:2496px" viewBox="0 0 100 100"><circle cx="50" cy="50" r="48" fill="none" stroke="#f6c41d" stroke-dasharray="2 3"/><circle cx="50" cy="50" r="43" fill="#f6c41d"/><circle cx="45" cy="54" r="13" fill="none" stroke="#fff" stroke-width="7" stroke-dasharray="5 3"/><circle cx="62" cy="38" r="8" fill="none" stroke="#fff" stroke-width="5" stroke-dasharray="4 2"/></svg>
  <svg class="abs service-icon" style="left:659px;top:2496px" viewBox="0 0 100 100"><circle cx="50" cy="50" r="48" fill="none" stroke="#f6c41d" stroke-dasharray="2 3"/><circle cx="50" cy="50" r="43" fill="#f6c41d"/><g fill="none" stroke="#fff" stroke-width="3"><ellipse cx="50" cy="50" rx="20" ry="8"/><ellipse cx="50" cy="50" rx="20" ry="8" transform="rotate(60 50 50)"/><ellipse cx="50" cy="50" rx="20" ry="8" transform="rotate(-60 50 50)"/></g><circle cx="50" cy="50" r="4" fill="#fff"/></svg>
  <svg class="abs service-icon" style="left:924px;top:2496px" viewBox="0 0 100 100"><circle cx="50" cy="50" r="48" fill="none" stroke="#f6c41d" stroke-dasharray="2 3"/><circle cx="50" cy="50" r="43" fill="#f6c41d"/><circle cx="45" cy="54" r="13" fill="none" stroke="#fff" stroke-width="7" stroke-dasharray="5 3"/><circle cx="62" cy="38" r="8" fill="none" stroke="#fff" stroke-width="5" stroke-dasharray="4 2"/></svg>

  <div class="abs service center" style="left:86px;top:2624px;width:280px"><h3>CLOSED CAPTIONING SERVICE</h3><p style="margin-top:8px">Fast, Accurate, and Inexpensive<br>Broadcast Quality Offline, Live, and<br>and Streamwell Content.</p></div>
  <div class="abs service center" style="left:356px;top:2624px;width:220px"><h3>SUBTITLING</h3><p style="margin-top:8px">We work to close your loan as<br>quickly as possible. We can even<br>hit curveballs!</p></div>
  <div class="abs service center" style="left:574px;top:2624px;width:270px"><h3>POST PRODUCTION SCRIPTS</h3><p style="margin-top:8px">Highly Detailed Post Production<br>Scripts — CCSL, CDSL, ABS, Dialogue &amp;<br>Spotting Lists</p></div>
  <div class="abs service center" style="left:844px;top:2624px;width:260px"><h3>AUDIO DESCRIPTION</h3><p style="margin-top:8px">High-End Encoding and Delivery of<br>Closed Captioning and Subtitling to<br>.mp2, .mov pro-res.</p></div>
</section>

<section>
  <div class="abs partners"></div>
  <svg class="abs arrow-btn" style="left:78px;top:2881px" viewBox="0 0 48 48"><circle cx="24" cy="24" r="23" fill="#f6c41d"/><path d="M32 24H16m6-6l-6 6 6 6" stroke="#fff" stroke-width="2.5" fill="none"/></svg>
  <svg class="abs arrow-btn" style="left:1084px;top:2881px" viewBox="0 0 48 48"><circle cx="24" cy="24" r="23" fill="#f6c41d"/><path d="M16 24h16m-6-6l6 6-6 6" stroke="#fff" stroke-width="2.5" fill="none"/></svg>
  <span class="abs partner" style="left:150px">Tidewell</span>
  <span class="abs partner" style="left:338px;color:#444">Marsh Hollow</span>
  <span class="abs partner" style="left:540px;color:#d84a3a">Rimstone</span>
  <span class="abs partner" style="left:722px;color:#2aa5a0">Lumen Baths</span>
  <span class="abs partner" style="left:912px">Longwave Pools</span>
</section>

<section>
  <div class="abs news"></div>
  <h2 class="abs h2 center" style="left:0;top:3022px;width:1200px">Recent News Articles</h2>
  <div class="abs news-card" style="left:93px;top:3117px;width:498px;height:494px">
    <div role="img" aria-label="Photo of a man in a suit signing papers at a desk" style="height:244px;background:linear-gradient(135deg,#8a8580,#d8d4cf 60%,#5a5550)"></div>
    <p class="date abs" style="left:19px;top:276px">Mon 09 , 11 , 2020</p>
    <p class="news-title abs" style="left:19px;top:308px;width:440px">Our expert IT staff have&nbsp; years of experience important IT specialties</p>
    <p class="news-text abs" style="left:19px;top:368px;width:450px">We're proud of the great culture we've developed here, combines professionalism, a friendly face, communications&nbsp; our own.</p>
  </div>
  <div class="abs news-card" style="left:606px;top:3130px;width:517px;height:140px">
    <div role="img" aria-label="Photo of police officers on a street" style="position:absolute;left:0;top:0;width:213px;height:140px;background:linear-gradient(135deg,#6f7a80,#c9c5b8)"></div>
    <p class="date abs" style="left:241px;top:14px">Mon 09 , 11 , 2020</p>
    <p class="news-title abs" style="left:241px;top:38px">Important IT specialties</p>
    <p class="news-text abs" style="left:241px;top:72px;width:260px">We're proud of the great culture developed ,within our own.</p>
  </div>
  <div class="abs news-card" style="left:606px;top:3293px;width:517px;height:140px">
    <div role="img" aria-label="Photo of officers in high-visibility vests at a gate" style="position:absolute;left:0;top:0;width:213px;height:140px;background:linear-gradient(135deg,#3a3a3a,#7a8a5a 60%,#2a2a2a)"></div>
    <p class="date abs" style="left:241px;top:14px">Mon 09 , 11 , 2020</p>
    <p class="news-title abs" style="left:241px;top:38px">Important IT specialties</p>
    <p class="news-text abs" style="left:241px;top:72px;width:260px">We're proud of the great culture developed ,within our own.</p>
  </div>
  <div class="abs news-card" style="left:606px;top:3456px;width:517px;height:140px">
    <div role="img" aria-label="Photo of two people in a meeting" style="position:absolute;left:0;top:0;width:213px;height:140px;background:linear-gradient(135deg,#3a3430,#b8aca0 60%,#e8e0d8)"></div>
    <p class="date abs" style="left:241px;top:14px">Mon 09 , 11 , 2020</p>
    <p class="news-title abs" style="left:241px;top:38px">Important IT specialties</p>
    <p class="news-text abs" style="left:241px;top:72px;width:260px">We're proud of the great culture developed ,within our own.</p>
  </div>
  <svg class="abs arrow-btn" style="left:547px;top:3642px" viewBox="0 0 48 48"><circle cx="24" cy="24" r="23" fill="#f6c41d"/><path d="M32 24H16m6-6l-6 6 6 6" stroke="#fff" stroke-width="2.5" fill="none"/></svg>
  <svg class="abs arrow-btn" style="left:615px;top:3642px" viewBox="0 0 48 48"><circle cx="24" cy="24" r="23" fill="#f6c41d"/><path d="M16 24h16m-6-6l6 6-6 6" stroke="#fff" stroke-width="2.5" fill="none"/></svg>
</section>

<footer>
  <div class="abs footer">
    <h4 style="left:183px;top:106px">Quick <span>Links</span></h4>
    <h4 style="left:466px;top:106px">Customer <span>Services</span></h4>
    <h4 style="left:732px;top:104px">Our <span>Newsletter</span></h4>
    <div class="abs rule" style="left:183px;top:146px"></div>
    <div class="abs rule" style="left:466px;top:146px"></div>
    <div class="abs rule" style="left:732px;top:146px"></div>

    <div class="abs" style="left:186px;top:188px;display:grid;row-gap:11px">
      <span class="flink">›&nbsp;Home</span><span class="flink">›&nbsp;About Us</span><span class="flink">›&nbsp;Our Services</span><span class="flink">›&nbsp;Our Blogs</span><span class="flink">›&nbsp;Talk To Us</span>
    </div>
    <div class="abs" style="left:470px;top:188px;display:grid;row-gap:11px">
      <span class="flink">›&nbsp;Closed Captioning</span><span class="flink">›&nbsp;Subtitling</span><span class="flink">›&nbsp;CCSL and Dialogue Lists</span><span class="flink">›&nbsp;Audio Description</span>
    </div>

    <div class="abs contact-row" style="left:736px;top:196px">
      <svg class="contact-icon" viewBox="0 0 34 34"><rect x="1" y="1" width="32" height="32" rx="6" fill="none" stroke="#fff" stroke-width="1.5"/><path d="M12 10l3 0 1.5 4-2 1.5a9 9 0 0 0 4 4l1.5-2 4 1.5v3a2 2 0 0 1-2 2A14 14 0 0 1 10 12a2 2 0 0 1 2-2z" fill="#fff"/></svg>
      <div>CALL US<br>(555) 014-2290</div>
    </div>
    <div class="abs contact-row" style="left:736px;top:250px">
      <svg class="contact-icon" viewBox="0 0 34 34"><rect x="1" y="1" width="32" height="32" rx="6" fill="none" stroke="#fff" stroke-width="1.5"/><rect x="10" y="12" width="14" height="10" fill="#fff"/><path d="M10 12l7 5 7-5" stroke="#2b7c7e" stroke-width="1.3" fill="none"/></svg>
      <div>EMAIL US<br>TalkToUs@QuilledMarkSubtitles.com</div>
    </div>
    <div class="abs contact-row" style="left:736px;top:306px">
      <svg class="contact-icon" viewBox="0 0 34 34"><rect x="1" y="1" width="32" height="32" rx="6" fill="none" stroke="#fff" stroke-width="1.5"/><path d="M17 26s-6-7-6-11a6 6 0 0 1 12 0c0 4-6 11-6 11z" fill="#fff"/><circle cx="17" cy="15" r="2.2" fill="#2b7c7e"/></svg>
      <div>Quilled Mark, LLC<br>4820 Harbor Lane Ste. 210 Fairview,<br>MD 20900</div>
    </div>
  </div>
  <div class="abs bottom">
    <svg class="abs social" style="left:97px;top:34px" viewBox="0 0 42 42" role="img" aria-label="Video channel"><circle cx="21" cy="21" r="19.5" fill="none" stroke="#fff" stroke-width="2"/><path d="M17 14.5v13l11-6.5z" fill="#fff"/></svg>
    <svg class="abs social" style="left:149px;top:34px" viewBox="0 0 42 42" role="img" aria-label="Chat with us"><circle cx="21" cy="21" r="19.5" fill="none" stroke="#fff" stroke-width="2"/><path d="M12 14h18a2 2 0 0 1 2 2v9a2 2 0 0 1-2 2h-9l-5 4v-4h-4a2 2 0 0 1-2-2v-9a2 2 0 0 1 2-2z" fill="#fff"/></svg>
    <svg class="abs social" style="left:200px;top:34px" viewBox="0 0 42 42" role="img" aria-label="Share"><circle cx="21" cy="21" r="19.5" fill="none" stroke="#fff" stroke-width="2"/><g fill="#fff"><circle cx="14" cy="21" r="3.2"/><circle cx="27" cy="14" r="3.2"/><circle cx="27" cy="28" r="3.2"/></g><path d="M14 21l13-7M14 21l13 7" stroke="#fff" stroke-width="2"/></svg>
    <svg class="abs social" style="left:252px;top:34px" viewBox="0 0 42 42" role="img" aria-label="Email newsletter"><circle cx="21" cy="21" r="19.5" fill="none" stroke="#fff" stroke-width="2"/><rect x="12" y="15" width="18" height="12" fill="#fff"/><path d="M12 15l9 7 9-7" stroke="#f6c41d" stroke-width="1.6" fill="none"/></svg>
    <p class="abs" style="right:78px;top:46px;font-size:14px;color:#fff">All Rights Reserved @ Copyrights 2023</p>
  </div>
</footer>

</body>
</html>
```